Our company needs a Corporate Identity Package!!!

We would like to receive submissions for a corporate identity pachage including the following elements:

1. Presentation Folder
2. Product/Service Catalogue (16 A4 pages landscape but expandable)
3. Product Brochure (up to 8 A4 pages)
4. Product Flyer (2 A4 pages)
5. Business Card
6. Letterhead
7. Envelope
8. E-mail signature.

I attach a Presentation Folder that i like (geometric but also has circle). We would like to have some ideas regarding the above 7 elements including brintavex logo colors (brintavex.example).

Payment is indicative and we are planning to increase the payment now that we found out how to actually do this. You are also more than welcome to send us a message and suggest the amount of payment for your Corporate Identity elements and we will update this.

Target Market(s)

Home | Office | Life

Colors
f78f20
0555a3
9bcb3b

Requirements
Must have
• 1. Presentation Folder
• 2. Product/Service Catalogue (16 A4 pages landscape but to be easily expandable)
• 3. Product Brochure (up to 4 A4 pages but to be easily expandable )
• 4. Product Flyer (2 A4 pages)
• 5. Business Card
• 6. Letterhead
• 7. Envelope
• 8. E-mail signature.
Nice to have
• It would be nice to include design something around the cycle that communicates the best six doctors (i.e. sunshine, water, rest, air, exercise and diet) !!!

```html
<!DOCTYPE html>
<html lang="en">
<head>
<meta charset="utf-8">
<title>brintavex – e-mail signature</title>
<link rel="stylesheet" href="https://fonts.googleapis.com/css2?family=Open+Sans:wght@400;600;700&display=swap">
<style>
  :root {
    --bg: #ffffff;
    --brand-blue: #0f8bd9;
    --deep-blue: #0555a3;
    --accent-orange: #f26522;
    --text-dark: #333333;
    --icon-blue: #1a8fdc;
  }
  html, body {
    margin: 0;
    padding: 0;
    overflow: hidden;
    background: var(--bg);
  }
  .signature {
    position: relative;
    width: 1200px;
    height: 502px;
    background: var(--bg);
    font-family: "Open Sans", Arial, sans-serif;
    color: var(--text-dark);
    overflow: hidden;
  }
  .brand-mark {
    position: absolute;
    left: 40px;
    top: 228px;
    display: flex;
    align-items: center;
    gap: 14px;
  }
  .brand-mark__dot {
    width: 64px;
    height: 64px;
    border-radius: 50%;
    background: var(--deep-blue);
  }
  .brand-mark__name {
    font-size: 34px;
    font-weight: 700;
    color: var(--deep-blue);
    letter-spacing: 0.5px;
  }
  .divider {
    position: absolute;
    left: 354px;
    top: 131px;
    width: 7px;
    height: 288px;
    background: var(--brand-blue);
  }
  .details {
    position: absolute;
    left: 402px;
    top: 116px;
    width: 780px;
  }
  .details__header {
    display: flex;
    align-items: baseline;
    gap: 30px;
    margin: 0 0 16px;
  }
  .details__name {
    font-size: 38px;
    font-weight: 700;
    color: var(--brand-blue);
    letter-spacing: 0.5px;
  }
  .details__market {
    font-size: 25px;
    font-weight: 600;
    color: var(--text-dark);
  }
  .details__address {
    font-size: 24px;
    font-weight: 600;
    line-height: 41px;
    margin: 0 0 12px;
  }
  .details__line {
    font-size: 24px;
    font-weight: 600;
    line-height: 44px;
    margin: 0;
    white-space: nowrap;
    letter-spacing: -0.2px;
  }
  .details__sep {
    margin: 0 10px;
  }
  .details__label {
    color: var(--accent-orange);
  }
  .social {
    display: flex;
    gap: 20px;
    margin-top: 18px;
    padding: 0;
    list-style: none;
  }
  .social__item {
    width: 34px;
    height: 34px;
    border: 2.5px solid var(--icon-blue);
    border-radius: 50%;
    box-sizing: border-box;
  }
</style>
</head>
<body>
  <div class="signature">
    <div class="brand-mark">
      <span class="brand-mark__dot"></span>
      <span class="brand-mark__name">brintavex</span>
    </div>

    <div class="divider"></div>

    <div class="details">
      <div class="details__header">
        <span class="details__name">brintavex</span>
        <span class="details__market">Home | Office | Life</span>
      </div>
      <p class="details__address">1580 Lane, Cedar Court, Suite 410, Millbrook,<br>Rivervale, USA 550219</p>
      <p class="details__line">t +1 (555) 014 - 237<span class="details__sep">|</span>m 0555 - 019 - 482</p>
      <p class="details__line"><span class="details__label">mail:</span> contact@halven.example<span class="details__sep">|</span><span class="details__label">website:</span> www.brintavex.example</p>
      <ul class="social" aria-label="Social profiles">
        <li class="social__item"></li>
        <li class="social__item"></li>
        <li class="social__item"></li>
        <li class="social__item"></li>
      </ul>
    </div>
  </div>
</body>
</html>
```